Custom Home Builder Needs a Website

Harbor Stone Builders Ltd. requires a clean professional 5 page website - Home, About Us, Gallery (Interior and Exterior), Our Process and Contact Us(with registration form). We are a home builder who also has homes for sale. Also please have a place for video embedding. Editable fields by user. Using the stationery 'feel' that is attached. Need social media links. If you require any additional files, please request.

Target Market(s)

Families and professionals

Industry/Entity Type

Home Builder

Coding

Coded - Design and coding required

Number of Pages Required

5+ page

Font styles to use
Sans Serif
Other font styles liked:
• Lato

Requirements
Must have
• Editable by user
• Register Button
• Place to put home models for sale - preferably on the first page
• 5 page website -
• -Home
• -About Us
• -Gallery (Interior and Exterior)
• -Our Process
• -Contact Us.
Nice to have
• Themed similar to current stationery
• place for video embedding
• Try some darker backgrounds
• Change pictures to B/W if works for design
Should not have
• cartoonish type of content

```html
<!DOCTYPE html>
<html lang="en">
<head>
<meta charset="utf-8">
<title>Harbor Stone Builders Ltd.</title>
<link href="https://fonts.googleapis.com/css2?family=Lato:wght@300;400;700&family=Raleway:wght@400;500&display=swap" rel="stylesheet">
<style>
:root{
  --green:#0a7a3a;
  --green-dark:#066a30;
  --lime:#34c91a;
  --ink:#333;
  --muted:#888;
  --light:#f4f4f4;
  --field:#f3f3f3;
  --white:#fff;
  --blue:#29aee0;
  --olive:#8cc02a;
  --amber:#f6a723;
  --tan:#c7a97b;
  --rose:#e0676a;
  --azure:#3a8fd6;
}
*{margin:0;padding:0;box-sizing:border-box}
html,body{width:1200px;height:3020px;overflow:hidden;background:var(--white)}
body{font-family:"Lato",sans-serif;color:var(--ink);position:relative}
.topbar{position:absolute;left:0;top:0;width:1200px;height:60px;background:var(--light)}
.brand{position:absolute;left:48px;top:14px;display:flex;align-items:center;gap:10px;font-weight:700;font-size:20px;color:var(--green)}
.brand-mark{width:28px;height:28px;background:var(--green)}
.account{position:absolute;right:52px;top:20px;display:flex;gap:44px;font-family:"Raleway",sans-serif;font-size:15px;color:var(--muted)}
.account span{display:flex;align-items:center;gap:8px}
.nav{position:absolute;left:0;top:60px;width:1200px;height:77px;background:var(--white);border-bottom:1px solid #e6e6e6}
.menu{position:absolute;left:48px;top:0;display:flex;height:77px;font-family:"Raleway",sans-serif;font-size:13px;color:#555}
.menu a{display:flex;align-items:center;padding:0 28px;position:relative;text-decoration:none;color:inherit}
.menu a+a::before{content:"";position:absolute;left:0;top:28px;height:20px;border-left:1px solid #ddd}
.menu a.active{color:var(--green)}
.menu a.active::after{content:"";position:absolute;left:0;right:0;bottom:0;height:4px;background:var(--green)}
.hotline{position:absolute;right:52px;top:10px;display:flex;gap:14px;align-items:center}
.hotline-number{font-size:29px;color:var(--green);line-height:1}
.hotline-mail{font-size:13px;color:#666;margin-top:4px}
.hero{position:absolute;left:0;top:137px;width:1200px;height:592px;background:linear-gradient(180deg,#7c8088 0%,#8a8a86 40%,#6d6658 70%,#4f5347 100%)}
.hero-text{position:absolute;left:0;right:0;top:228px;text-align:center;color:var(--white)}
.hero-text h1{font-size:33px;font-weight:700}
.hero-text p{font-size:27px;font-weight:300;margin-top:6px}
.thumbs{position:absolute;left:104px;top:467px;display:flex;gap:7px}
.thumb{width:172px;height:105px;border:3px solid #ddd}
.thumb.current{border-color:var(--white)}
.arrow{position:absolute;top:467px;width:20px;height:105px;background:rgba(0,0,0,.55);display:flex;align-items:center;justify-content:center}
.about{position:absolute;left:0;top:729px;width:1200px;height:269px;background:linear-gradient(180deg,var(--green),var(--green-dark))}
.about-photo{position:absolute;left:89px;top:48px;width:269px;height:157px;background:linear-gradient(180deg,#c8d0d6,#9aa09a 60%,#3a3f44)}
.about-body{position:absolute;left:439px;top:58px;width:640px;color:var(--white)}
.about-body h2{font-size:20px;font-weight:700}
.about-body p{font-size:12.5px;line-height:1.45;margin-top:10px}
.btn-outline{display:inline-block;margin-top:16px;border:2px solid var(--white);padding:6px 18px;font-size:12px}
.section-title{position:absolute;left:0;right:0;text-align:center;font-size:24px;color:#333;font-weight:400;z-index:2}
.gallery-sub{position:absolute;left:0;right:0;top:1114px;text-align:center;font-size:12.5px;color:var(--muted)}
.tabs{position:absolute;left:108px;top:1164px;display:flex;gap:32px;font-size:12px;color:var(--muted);align-items:center}
.tabs .on{color:var(--green);border-top:3px solid var(--green);padding-top:10px}
.tabs .dot{width:4px;height:4px;border-radius:50%;background:#999;margin-top:12px}
.tabs span{padding-top:13px}
.view-all{position:absolute;left:998px;top:1166px;width:116px;height:38px;border:2px solid #444;font-size:12px;display:flex;align-items:center;justify-content:center}
.gallery-grid{position:absolute;left:87px;top:1228px;display:flex;gap:17px}
.gallery-item{width:245px;height:244px;border:1px solid #ddd}
.process{position:absolute;left:0;top:1542px;width:1200px;height:640px;background:#f7f7f7;z-index:0}
.swoosh{position:absolute;left:0;top:1990px;z-index:1}
.step{position:absolute;width:240px;text-align:center;font-size:15px;line-height:1.35;color:#333;z-index:2}
.step svg{display:block;margin:0 auto 8px}
.divider{position:absolute;width:1px;height:90px;background:#e2e2e2;z-index:2}
.field{position:absolute;background:var(--field);font-size:12px;color:#999;padding:0 35px;display:flex;align-items:center}
.send{position:absolute;left:531px;top:2550px;width:117px;height:37px;background:var(--green);color:var(--white);font-size:13px;font-weight:700;display:flex;align-items:center;justify-content:center}
.footer{position:absolute;left:0;top:2691px;width:1200px;height:288px;background:#f0f0f0}
.fcol{position:absolute;top:54px}
.fcol h3{font-size:20px;font-weight:400;color:#333;margin-bottom:12px}
.fcol li{list-style:none;font-size:15px;line-height:20px;color:#444}
.phone-lg{font-size:20px!important;margin-bottom:4px}
.email-field{width:202px;height:28px;background:var(--white);font-size:10px;color:#888;padding:7px 12px}
.subscribe{margin:8px 0 0 122px;width:80px;height:23px;background:var(--green);color:var(--white);font-size:10px;font-weight:700;display:flex;align-items:center;justify-content:center}
.socials{display:flex;gap:6px;margin-left:4px}
.socials i{width:28px;height:28px;border-radius:50%}
.copyright{position:absolute;left:0;top:2979px;width:1200px;height:41px;background:var(--green);color:var(--white);font-size:13px;padding:13px 89px}
</style>
</head>
<body>

<header class="topbar">
  <div class="brand"><span class="brand-mark"></span>Harbor Stone Builders Ltd.</div>
  <div class="account">
    <span><svg width="14" height="14" viewBox="0 0 14 14"><circle cx="6" cy="4" r="3" fill="none" stroke="#999"/><path d="M1 13c0-4 10-4 10 0" fill="none" stroke="#999"/></svg>Register</span>
    <span><svg width="14" height="14" viewBox="0 0 14 14"><path d="M8 2h4v10H8M1 7h8M6 4l3 3-3 3" fill="none" stroke="#999"/></svg>Login</span>
  </div>
</header>

<nav class="nav">
  <div class="menu">
    <a class="active">Home</a>
    <a>About Us</a>
    <a>Gallery &#9662;</a>
    <a>Our Process</a>
    <a>Contact Us</a>
  </div>
  <div class="hotline">
    <svg width="40" height="40" viewBox="0 0 40 40"><path d="M10 6l7 7-4 4c2 5 6 9 11 11l4-4 7 7-5 5C18 34 6 22 5 11z" fill="#0a7a3a"/><path d="M24 6a10 10 0 0 1 10 10M24 12a4 4 0 0 1 4 4" fill="none" stroke="#0a7a3a" stroke-width="2.5"/></svg>
    <div>
      <div class="hotline-number">+123-456-7890</div>
      <div class="hotline-mail">info@harborstonebuilders.com</div>
    </div>
  </div>
</nav>

<section class="hero" role="img" aria-label="Two-storey stone and shingle family home under an overcast sky">
  <div class="hero-text">
    <h1>Contrary to popular belief</h1>
    <p>Lorem Ipsum is not simply random text</p>
  </div>
  <div class="arrow" style="left:0"><svg width="10" height="16"><path d="M8 2L2 8l6 6" stroke="#fff" stroke-width="2" fill="none"/></svg></div>
  <div class="thumbs">
    <div class="thumb current" role="img" aria-label="Home exterior" style="background:linear-gradient(#8a8e94,#6c6656 60%,#5b6a4a)"></div>
    <div class="thumb" role="img" aria-label="Row of homes" style="background:linear-gradient(#c9d2da,#6e6a64 60%,#777)"></div>
    <div class="thumb" role="img" aria-label="Home with blue sky" style="background:linear-gradient(#7fa6d6,#5a5c62 60%,#6d7a54)"></div>
    <div class="thumb" role="img" aria-label="Bright kitchen" style="background:linear-gradient(#e9e6df,#c9c3b6 60%,#8d8070)"></div>
    <div class="thumb" role="img" aria-label="Office room" style="background:linear-gradient(#dcdad6,#b9b4ac 60%,#6a4d36)"></div>
    <div class="thumb" role="img" aria-label="Kitchen backsplash" style="background:linear-gradient(#8b6a4c,#5a4638 60%,#c9a07a)"></div>
  </div>
  <div class="arrow" style="right:0"><svg width="10" height="16"><path d="M2 2l6 6-6 6" stroke="#fff" stroke-width="2" fill="none"/></svg></div>
</section>

<section class="about">
  <div class="about-photo" role="img" aria-label="Portrait of the company founder outdoors"></div>
  <div class="about-body">
    <h2>ABOUT US</h2>
    <p>Lorem Ipsum is simply dummy text of the printing and typesetting industry. Lorem Ipsum has been the industry's standard dummy text ever since the 1500s, when an unknown printer took a galley of type and scrambled it to make a type specimen book.</p>
    <span class="btn-outline">READ MORE</span>
  </div>
</section>

<h2 class="section-title" style="top:1072px">GALLERY</h2>
<p class="gallery-sub">Lorem Ipsum is simply dummy text of the printing and typesetting industry.</p>
<div class="tabs"><span class="on">EXTERIOR</span><i class="dot"></i><span>INTERIOR</span></div>
<div class="view-all">VIEW ALL</div>
<div class="gallery-grid">
  <div class="gallery-item" role="img" aria-label="Dark grey home with lawn" style="background:linear-gradient(#c7d3df,#4f5358 55%,#4f7a36)"></div>
  <div class="gallery-item" role="img" aria-label="Stone-front home with tree" style="background:linear-gradient(#dfe4e8,#6b6c66 55%,#8a8a84)"></div>
  <div class="gallery-item" role="img" aria-label="Grey home with driveway" style="background:linear-gradient(#a9bfd6,#5b5f66 55%,#6f6d68)"></div>
  <div class="gallery-item" role="img" aria-label="Blue-grey home with garden" style="background:linear-gradient(#7fa6d8,#5a6470 55%,#8a7a5c)"></div>
</div>

<section class="process"></section>
<svg class="swoosh" width="1200" height="240" viewBox="0 0 1200 240" aria-hidden="true">
  <path d="M0 0C150 90 500 170 1200 155V240H0z" fill="#fff"/>
  <path d="M0 124C200 170 500 205 790 217C500 230 200 222 0 186z" fill="var(--lime)"/>
</svg>
<h2 class="section-title" style="top:1601px">OUR PROCESS</h2>

<div class="step" style="left:73px;top:1686px">
  <svg width="150" height="134" viewBox="0 0 150 134"><circle cx="75" cy="67" r="64" fill="none" stroke="var(--blue)" stroke-width="2"/><path d="M132 60l12 7-12 7z" fill="var(--blue)"/><circle cx="75" cy="67" r="58" fill="var(--blue)"/><rect x="52" y="52" width="40" height="30" fill="none" stroke="#fff" stroke-width="3"/><path d="M72 76l28-28" stroke="#fff" stroke-width="5"/></svg>
  Decide on<br>the design theme
</div>
<div class="divider" style="left:343px;top:1690px"></div>
<div class="step" style="left:357px;top:1686px">
  <svg width="150" height="134" viewBox="0 0 150 134"><circle cx="75" cy="67" r="64" fill="none" stroke="var(--olive)" stroke-width="2"/><path d="M132 60l12 7-12 7z" fill="var(--olive)"/><circle cx="75" cy="67" r="58" fill="var(--olive)"/><path d="M50 68l25-22 25 22v20H50z" fill="none" stroke="#fff" stroke-width="4"/><rect x="64" y="70" width="22" height="10" fill="#fff"/></svg>
  Decide on<br>the interior designer
</div>
<div class="divider" style="left:600px;top:1690px"></div>
<div class="step" style="left:625px;top:1686px">
  <svg width="150" height="134" viewBox="0 0 150 134"><circle cx="75" cy="67" r="64" fill="none" stroke="var(--amber)" stroke-width="2"/><path d="M132 60l12 7-12 7z" fill="var(--amber)"/><circle cx="75" cy="67" r="58" fill="var(--amber)"/><path d="M48 70l27-24 27 24M56 64v24h38V64" fill="none" stroke="#fff" stroke-width="4"/></svg>
  Start<br>Renovation
</div>
<div class="divider" style="left:888px;top:1690px"></div>
<div class="step" style="left:895px;top:1686px">
  <svg width="150" height="134" viewBox="0 0 150 134"><circle cx="75" cy="67" r="64" fill="none" stroke="var(--tan)" stroke-width="2"/><circle cx="75" cy="67" r="58" fill="var(--tan)"/><path d="M52 90l12-24h22l12 24z" fill="#fff"/><path d="M75 42l3 7 7 3-7 3-3 7-3-7-7-3 7-3z" fill="#fff"/></svg>
  Purchase<br>Home Decor Appliances
</div>

<div class="step" style="left:77px;top:1912px">
  <svg width="150" height="134" viewBox="0 0 150 134"><circle cx="75" cy="67" r="64" fill="none" stroke="var(--rose)" stroke-width="2"/><path d="M132 60l12 7-12 7z" fill="var(--rose)"/><circle cx="75" cy="67" r="58" fill="var(--rose)"/><circle cx="75" cy="62" r="14" fill="none" stroke="#fff" stroke-width="4"/><path d="M52 90h46M60 46l30 40" stroke="#fff" stroke-width="4"/></svg>
  Defects<br>Inspection
</div>
<div class="divider" style="left:343px;top:1916px"></div>
<div class="step" style="left:357px;top:1912px">
  <svg width="150" height="134" viewBox="0 0 150 134"><circle cx="75" cy="67" r="64" fill="none" stroke="var(--azure)" stroke-width="2"/><path d="M132 60l12 7-12 7z" fill="var(--azure)"/><circle cx="75" cy="67" r="58" fill="var(--azure)"/><path d="M70 52H54v36h36V74" fill="none" stroke="#fff" stroke-width="4"/><path d="M66 76c2-14 12-20 24-20v-8l12 12-12 12v-8c-10 0-18 4-24 12z" fill="#fff"/></svg>
  Moving In
</div>

<h2 class="section-title" style="top:2322px">CONTACT US</h2>
<div class="field" style="left:266px;top:2381px;width:322px;height:45px">Enter Your Name</div>
<div class="field" style="left:598px;top:2381px;width:314px;height:45px">Email Address</div>
<div class="field" style="left:266px;top:2436px;width:646px;height:90px;align-items:flex-start;padding-top:18px">Email Address</div>
<div class="send">SEND</div>

<footer class="footer">
  <div class="fcol" style="left:89px">
    <h3>QUICK LINKS</h3>
    <ul><li>Home</li><li>About Us</li><li>Galery</li><li>Our Process</li><li>Contact Us</li></ul>
  </div>
  <div class="fcol" style="left:320px">
    <h3>CONTACT US</h3>
    <ul><li class="phone-lg">123-456-7980</li><li>E: info@harborstonebuilders.com</li><li>A: 214 W. Alder Ridge Rd.</li><li>Northfield, MN 55057</li></ul>
  </div>
  <div class="fcol" style="left:654px">
    <h3>NEWSLETTER</h3>
    <div class="email-field">Enter your email..</div>
    <div class="subscribe">SUBSCRIBE</div>
  </div>
  <div class="fcol" style="left:960px">
    <h3>SOCIAL MEDIA</h3>
    <div class="socials"><i style="background:#3b5998"></i><i style="background:#2fa3dc"></i><i style="background:#9a7a5e"></i><i style="background:#d6372e"></i></div>
  </div>
</footer>
<div class="copyright">Copyright 2016. Harborstonebuilders All Rights Reserved.</div>

</body>
</html>
```